South Carolina Bridal and Formal Wear Store

We want The Gown Parlor of Ashcombe website to feel luxurious, elegant, welcoming, and approachable—without feeling overpriced or intimidating. The site should immediately show that we are a full-service bridal and formal wear destination, offering bridal gowns, prom, mothers’ dresses, tuxedos and suits, accessories, and more. We want beautiful, high-end imagery and a clean, modern design while still reflecting the warm, personal experience customers receive when they walk into our boutique. Most importantly, the website should be easy to shop and navigate, allowing customers to browse our collections, see what we offer, understand price ranges, book appointments, and feel excited and comfortable choosing The Gown Parlor of Ashcombe for all of their special-event needs.

Target Market(s)

Women ages 18-50. Brides, engaged women, mothers of the occasion

Industry/Entity Type

Bridal and Formal Wear

Coding

Coded - Design and coding required

Number of Pages Required

5+ page

Font styles to use
Sans Serif

Colors

Designer to choose colors to be used in the design.

Requirements
Must have
• Appointment area, about us staff area, what we offer and designers our logo
Nice to have
• Modern Southern Luxury: Clean, elegant, and upscale with soft neutral tones, beautiful bridal photography, and a warm Lowcountry feel.
Should not have
• pricing

```html
<!DOCTYPE html>
<html lang="en">
<head>
<meta charset="utf-8">
<title>The Gown Parlor of Ashcombe — Formal Wear</title>
<link rel="stylesheet" href="https://fonts.googleapis.com/css2?family=Inter+Tight:wght@400;500;600;700&family=Inter:wght@400;500;600;700&display=swap">
<style>
  :root {
    --bg-header: #0d0d0d;
    --bg-section: #161616;
    --bg-footer: #0d0d0d;
    --text-main: #f4f1ec;
    --text-soft: #c3bcb3;
    --text-muted: #8f8980;
    --label: #a89f93;
    --cream: #efe7dc;
    --button-light: #f1eeea;
    --ink: #141414;
    --rule: #2a2a2a;
    --accent: #c9b89c;
  }
  * { margin: 0; padding: 0; box-sizing: border-box; }
  html, body { width: 1200px; height: 612px; overflow: hidden; background: var(--bg-footer); }
  body { position: relative; font-family: "Inter", sans-serif; color: var(--text-main); }

  .cta-section { position: absolute; left: 0; top: 0; width: 1200px; height: 322px; background: var(--bg-section); overflow: hidden; }
  .cta-arc { position: absolute; left: 0; top: 0; }
  .cta-heading {
    position: absolute; left: 166px; top: 26px;
    font-family: "Inter Tight", sans-serif; font-weight: 500;
    font-size: 44px; line-height: 48.5px; letter-spacing: -1.6px; color: #fff;
  }
  .cta-text { position: absolute; left: 167px; top: 186px; width: 370px; font-size: 13px; line-height: 23px; color: var(--text-soft); }
  .cta-button {
    position: absolute; left: 561px; top: 110px; width: 180px; height: 34px;
    background: var(--button-light); color: var(--ink);
    display: flex; align-items: center; justify-content: center; gap: 9px;
    font-size: 8px; font-weight: 700; letter-spacing: 1.3px; text-transform: uppercase; border-radius: 1px;
  }

  .site-header { position: absolute; left: 0; top: 0; width: 1200px; height: 42px; background: var(--bg-header); border-bottom: 1px solid #1c1c1c; }
  .brand-small { position: absolute; left: 122px; top: 11px; width: 120px; font-family: "Inter Tight", sans-serif; font-weight: 500; font-size: 9.5px; line-height: 10.5px; color: var(--text-main); letter-spacing: 0.2px; }
  .main-nav { position: absolute; top: 13px; left: 0; }
  .main-nav a { position: absolute; white-space: nowrap; font-size: 7.3px; font-weight: 600; letter-spacing: 1.3px; text-transform: uppercase; color: #cfc9c1; text-decoration: none; }
  .main-nav a.is-active { color: #fff; }
  .main-nav a.is-active::after { content: ""; position: absolute; left: 0; right: 0; top: 13px; height: 1px; background: var(--accent); }
  .header-button {
    position: absolute; left: 921px; top: 3px; width: 160px; height: 30px;
    background: var(--cream); color: var(--ink);
    display: flex; align-items: center; justify-content: center; gap: 9px;
    font-size: 7.8px; font-weight: 700; letter-spacing: 1.2px; text-transform: uppercase;
  }

  .site-footer { position: absolute; left: 0; top: 322px; width: 1200px; height: 290px; background: var(--bg-footer); }
  .brand-large { position: absolute; left: 172px; top: 68px; font-family: "Inter Tight", sans-serif; font-weight: 500; font-size: 24px; line-height: 27px; letter-spacing: -0.3px; color: var(--text-main); }
  .footer-about { position: absolute; left: 167px; top: 154px; width: 270px; font-size: 8.7px; line-height: 15.2px; color: var(--text-muted); }
  .footer-label { position: absolute; top: 56px; font-size: 7px; font-weight: 600; letter-spacing: 1.5px; text-transform: uppercase; color: var(--label); }
  .footer-links { position: absolute; top: 75px; list-style: none; }
  .footer-links li { font-size: 9.3px; line-height: 16.5px; color: var(--text-main); }
  .contact-strong { position: absolute; left: 778px; top: 75px; font-size: 9.3px; line-height: 16.5px; color: var(--text-main); }
  .contact-muted { position: absolute; left: 778px; font-size: 8.3px; line-height: 13.8px; color: var(--text-muted); }
  .footer-rule { position: absolute; left: 167px; top: 245px; width: 868px; height: 1px; background: var(--rule); }
  .footer-meta { position: absolute; top: 264px; font-size: 7px; letter-spacing: 1.1px; text-transform: uppercase; color: var(--text-muted); }
  .to-top { position: absolute; left: 1172px; top: 250px; }
</style>
</head>
<body>

<section class="cta-section">
  <svg class="cta-arc" width="1200" height="322" viewBox="0 0 1200 322" aria-hidden="true">
    <circle cx="1164" cy="-66" r="168" fill="none" stroke="#262626" stroke-width="1"/>
  </svg>
  <h2 class="cta-heading">Come find the<br>look everyone<br>remembers.</h2>
  <p class="cta-text">Prom, mothers and bridesmaid appointments are available through the boutique.</p>
  <a class="cta-button">Request an appointment
    <svg width="8" height="6" viewBox="0 0 8 6" aria-hidden="true"><path d="M0 3h7M4.5 0.5 7 3 4.5 5.5" fill="none" stroke="currentColor" stroke-width="1"/></svg>
  </a>
</section>

<header class="site-header">
  <div class="brand-small">The Gown Parlor<br>of Ashcombe</div>
  <nav class="main-nav">
    <a style="left:423px">Collections</a>
    <a class="is-active" style="left:509px">Formal Wear</a>
    <a style="left:598px">Tuxedos</a>
    <a style="left:663px">Designers</a>
    <a style="left:737px">The House</a>
  </nav>
  <a class="header-button">Request appointment
    <svg width="8" height="6" viewBox="0 0 8 6" aria-hidden="true"><path d="M0 3h7M4.5 0.5 7 3 4.5 5.5" fill="none" stroke="currentColor" stroke-width="1"/></svg>
  </a>
</header>

<footer class="site-footer">
  <div class="brand-large">The Gown Parlor<br>of Ashcombe</div>
  <p class="footer-about">A full-service bridal and formal wear boutique bringing modern Southern elegance, thoughtful styling and a warm Lowcountry welcome to every special occasion.</p>

  <div class="footer-label" style="left:511px">Explore</div>
  <ul class="footer-links" style="left:511px">
    <li>Bridal</li><li>Mothers</li><li>Tuxedos &amp; Suits</li><li>Appointments</li>
  </ul>
  <ul class="footer-links" style="left:627px">
    <li>Prom</li><li>Bridesmaids</li><li>Designers</li><li>Our House</li>
  </ul>

  <div class="footer-label" style="left:778px">Visit the boutique</div>
  <div class="contact-strong">843-555-0142<br>appointments@thegownparlorofashcombe.com</div>
  <div class="contact-muted" style="top:115px">240 Harbor Lane, Suite 12<br>Ashcombe, SC 29000</div>
  <div class="contact-muted" style="top:156px">Wednesday–Saturday · 10am–6pm<br>Sunday–Tuesday · Closed</div>

  <div class="footer-rule"></div>
  <div class="footer-meta" style="left:167px">© 2026 The Gown Parlor of Ashcombe · Design Concept</div>
  <div class="footer-meta" style="right:165px">Bridal · Tuxedos · Formal Wear</div>

  <svg class="to-top" width="28" height="28" viewBox="0 0 28 28" aria-label="Back to top" role="img">
    <circle cx="14" cy="14" r="13.5" fill="#ffffff"/>
    <path d="M14 21V7M9 12l5-5 5 5" fill="none" stroke="#111" stroke-width="1.8"/>
  </svg>
</footer>

</body>
</html>
```